Weinetiketten für unsere neue Weinlinie SOMMERGLUT
Zielgruppe
Wir stellen qualitativ sehr hochwertige Weine, Sekte und Destillate her.
Unsere Zielgruppe sind kaufkräftige Kunden zwischen 25-70 Jahren.
Aufgabenstellung
Edel, schlicht und zeitlos soll das neue Etikett werden, nur leicht verspielt.
Mit hohem Wiedererkennungswert, da die Wein auch im Fachhandel (in Regalen) präsentiert werden. Der Name "Sommerglut" steht für expressive Weine voller Fruchtaromen und Düften.

```html
<!DOCTYPE html>
<html lang="de">
<head>
<meta charset="utf-8">
<title>Sommerglut – Weinetikett</title>
<link rel="stylesheet" href="https://fonts.googleapis.com/css2?family=Marcellus&family=Kaushan+Script&family=Libre+Baskerville:ital@1&display=swap">
<style>
  :root {
    --backdrop: #a9a9a9;
    --paper-light: #f3f3f3;
    --paper-shade: #bdbdbd;
    --gold: #b8912f;
    --gold-dark: #7a4d12;
    --gold-light: #e6c77f;
    --script: #9a6a22;
    --ink: #1a1a1a;
  }
  * { margin: 0; padding: 0; box-sizing: border-box; }
  html, body { width: 1200px; height: 3001px; overflow: hidden; }
  body { background: var(--backdrop); position: relative; }

  .label {
    position: absolute;
    left: 100px; top: 715px;
    width: 1000px; height: 1571px;
    background: linear-gradient(90deg, var(--paper-light) 0%, var(--paper-shade) 45%, var(--paper-light) 85%, #fafafa 100%);
    border-left: 15px solid var(--gold);
    border-right: 15px solid var(--gold);
    font-family: "Marcellus", serif;
    overflow: hidden;
  }
  .label::before, .label::after {
    content: "";
    position: absolute; left: 0; right: 0; height: 19px;
    background: linear-gradient(90deg, var(--gold-dark), var(--gold-light) 45%, var(--gold) 70%, var(--gold-dark));
  }
  .label::before { top: 0; }
  .label::after { bottom: 0; }

  .label > * { position: absolute; }
  .winery-mark { left: 50%; top: 190px; transform: translateX(-50%); }
  .rule { top: 698px; height: 3px; background: var(--gold); }
  .rule--left { left: 94px; width: 345px; }
  .rule--right { left: 545px; width: 348px; }

  .winery-name {
    left: 0; right: 0; top: 730px; text-align: center;
    font-weight: 400; font-size: 76px; line-height: 1; color: var(--gold); letter-spacing: 2px;
  }
  .wine-name {
    left: 0; right: 0; top: 800px; text-align: center;
    font-family: "Kaushan Script", cursive; font-weight: 400;
    font-size: 160px; line-height: 1.2; color: var(--script);
    white-space: nowrap;
  }
  .grape {
    left: 0; right: 0; top: 1262px; text-align: center;
    font-size: 70px; line-height: 1; color: var(--ink); letter-spacing: 2px;
  }
  .style {
    left: 0; right: 0; top: 1340px; text-align: center;
    font-size: 42px; line-height: 1; color: #333;
  }
  .facts {
    left: 60px; right: 60px; top: 1430px;
    display: flex; justify-content: space-between; align-items: center;
    font-size: 34px; color: var(--ink);
  }
  .vintage {
    font-family: "Libre Baskerville", serif; font-style: italic;
    font-size: 58px; color: var(--gold);
  }
</style>
</head>
<body>
  <section class="label">
    <svg class="winery-mark" width="340" height="340" viewBox="0 0 340 340" role="img" aria-label="Weingut Falkenrain">
      <circle cx="170" cy="170" r="160" fill="var(--ink)" stroke="var(--gold)" stroke-width="8"/>
    </svg>
    <div class="rule rule--left"></div>
    <div class="rule rule--right"></div>
    <h2 class="winery-name">FALKENRAIN</h2>
    <h1 class="wine-name">Sommerglut</h1>
    <p class="grape">RIESLING</p>
    <p class="style">trocken</p>
    <div class="facts">
      <span class="volume">0.75L</span>
      <span class="vintage">2009</span>
      <span class="abv">12.5%Vol</span>
    </div>
  </section>
</body>
</html>
```